Spray Foam Company Business Card

We need a business card designed for our spray foam insulation and roof coatings business. We handle residential and commercial projects.
Industry/Entity Type
Construction
Contact Information for Business Card
We would like it to say:
K & R Coat
with these bullet points
-foam insulation
-waterproofing roof system
-water proofing foundation systems
website is krcoatfoamsealers.com (this was just purchased)
office phone : 630-555-0148
And 3 cards with names on them the names are :
Darren Hollis
Trevor Lindqvist
Neil Bruxton
maybe the bullet points can go on the back?
if you go this website it is another division of our company and you can see the font we use in the K & R. We do not want to use the same half circles that it has just the lettering
www.thesturdiestfinishwork.com
Look and feel
Each slider illustrates characteristics of the customer's brand and the style your logo design should communicate.

```html
<!DOCTYPE html>
<html lang="en">
<head>
<meta charset="utf-8">
<title>K &amp; R Coat — Business Cards</title>
<link rel="stylesheet" href="https://fonts.googleapis.com/css2?family=Fira+Sans:wght@400;600&display=swap">
<style>
  :root {
    --card-charcoal: #3f3e40;
    --band-black: #050505;
    --paper-white: #ffffff;
    --text-white: #ffffff;
    --ink-black: #111111;
    --figure-grey: #a7a9ac;
    --figure-grey-deep: #8f9194;
    --figure-white: #f2f2f2;
    --figure-white-deep: #d6d6d6;
  }
  * { margin: 0; padding: 0; box-sizing: border-box; }
  html, body {
    width: 1200px;
    height: 3136px;
    overflow: hidden;
    background: var(--paper-white);
  }
  .sheet {
    position: relative;
    width: 1200px;
    height: 3136px;
    background: var(--paper-white);
    font-family: "Fira Sans", Arial, sans-serif;
    color: var(--text-white);
  }
  .card {
    position: absolute;
    left: 0;
    width: 1200px;
    height: 692px;
    background: var(--card-charcoal);
    overflow: hidden;
  }
  .card--back { top: 0; height: 695px; }
  .card--darren { top: 737px; }
  .card--trevor { top: 1497px; }
  .card--neil { top: 2267px; }

  /* back of card */
  .services-band {
    position: absolute;
    left: 0;
    top: 413px;
    width: 1200px;
    height: 282px;
    background: var(--band-black);
  }
  .foam-spray {
    position: absolute;
    left: 560px;
    top: 0;
    width: 640px;
    height: 413px;
    background: radial-gradient(ellipse at 62% 40%, rgba(233,233,233,0.95) 0%, rgba(233,233,233,0.7) 45%, rgba(233,233,233,0) 75%);
  }
  .brand-oval {
    position: absolute;
    left: 652px;
    top: 55px;
    width: 482px;
    height: 296px;
    border-radius: 50%;
    background: var(--paper-white);
    display: flex;
    align-items: center;
    justify-content: center;
  }
  .brand-name {
    font-family: "Fira Sans", Arial, sans-serif;
    font-weight: 400;
    font-size: 100px;
    color: var(--ink-black);
    letter-spacing: 2px;
    white-space: nowrap;
  }
  .sprayer-figure {
    position: absolute;
    left: 0;
    top: 250px;
    width: 420px;
    height: 445px;
    background: linear-gradient(160deg, var(--figure-white) 0%, var(--figure-white-deep) 100%);
    border-top-right-radius: 180px;
  }
  .services {
    position: absolute;
    left: 500px;
    top: 458px;
    list-style: none;
    font-size: 47px;
    font-weight: 400;
    line-height: 65px;
    white-space: nowrap;
  }
  .services li {
    position: relative;
    padding-left: 40px;
  }
  .services li::before {
    content: "";
    position: absolute;
    left: 0;
    top: 26px;
    width: 22px;
    height: 22px;
    border: 3px solid var(--text-white);
    border-radius: 50%;
  }

  /* front cards */
  .worker-figure {
    position: absolute;
    left: 0;
    top: 160px;
    width: 460px;
    height: 532px;
    background: linear-gradient(150deg, var(--figure-grey) 0%, var(--figure-grey-deep) 100%);
    border-top-right-radius: 220px;
  }
  .person-name {
    position: absolute;
    top: 118px;
    font-size: 47px;
    font-weight: 600;
    text-transform: uppercase;
    letter-spacing: 0.5px;
    white-space: nowrap;
  }
  .card--darren .person-name { left: 538px; }
  .card--trevor .person-name { left: 518px; }
  .card--neil .person-name { left: 548px; }
  .contact {
    position: absolute;
    left: 476px;
    top: 385px;
    list-style: none;
    font-size: 48px;
    font-weight: 400;
    line-height: 66px;
    white-space: nowrap;
  }
  .contact li {
    display: flex;
    align-items: center;
  }
  .contact-icon {
    width: 40px;
    height: 40px;
    margin-right: 34px;
    flex: none;
  }
</style>
</head>
<body>
<main class="sheet">

  <section class="card card--back" aria-label="Card back with services">
    <div class="foam-spray" role="img" aria-label="Cloud of spray foam bubbles"></div>
    <div class="brand-oval"><span class="brand-name">K &amp; R</span></div>
    <div class="services-band"></div>
    <div class="sprayer-figure" role="img" aria-label="Silhouette of a worker in a respirator spraying foam"></div>
    <ul class="services">
      <li>foam insulation</li>
      <li>waterproofing roof system</li>
      <li>water proofing foundation</li>
    </ul>
  </section>

  <section class="card card--darren" aria-label="Darren Hollis card">
    <div class="worker-figure" role="img" aria-label="Grey silhouette of a worker holding a spray gun"></div>
    <h2 class="person-name">Darren Hollis</h2>
    <ul class="contact">
      <li><svg class="contact-icon" viewBox="0 0 40 40" fill="none" stroke="currentColor" stroke-width="3"><path d="M6 18c0-7 6-12 14-12s14 5 14 12-6 12-14 12c-2 0-4 0-6-1l-7 4 2-6c-2-2-3-5-3-9z"/></svg>630-555-0148</li>
      <li><svg class="contact-icon" viewBox="0 0 40 40" fill="none" stroke="currentColor" stroke-width="3"><rect x="5" y="8" width="30" height="20"/><path d="M14 33h12M20 28v5"/></svg>krcoatfoamsealers.com</li>
    </ul>
  </section>

  <section class="card card--trevor" aria-label="Trevor Lindqvist card">
    <div class="worker-figure" role="img" aria-label="Grey silhouette of a worker holding a spray gun"></div>
    <h2 class="person-name">Trevor Lindqvist</h2>
    <ul class="contact">
      <li><svg class="contact-icon" viewBox="0 0 40 40" fill="none" stroke="currentColor" stroke-width="3"><path d="M6 18c0-7 6-12 14-12s14 5 14 12-6 12-14 12c-2 0-4 0-6-1l-7 4 2-6c-2-2-3-5-3-9z"/></svg>630-555-0148</li>
      <li><svg class="contact-icon" viewBox="0 0 40 40" fill="none" stroke="currentColor" stroke-width="3"><rect x="5" y="8" width="30" height="20"/><path d="M14 33h12M20 28v5"/></svg>krcoatfoamsealers.com</li>
    </ul>
  </section>

  <section class="card card--neil" aria-label="Neil Bruxton card">
    <div class="worker-figure" role="img" aria-label="Grey silhouette of a worker holding a spray gun"></div>
    <h2 class="person-name">Neil Bruxton</h2>
    <ul class="contact">
      <li><svg class="contact-icon" viewBox="0 0 40 40" fill="none" stroke="currentColor" stroke-width="3"><path d="M6 18c0-7 6-12 14-12s14 5 14 12-6 12-14 12c-2 0-4 0-6-1l-7 4 2-6c-2-2-3-5-3-9z"/></svg>630-555-0148</li>
      <li><svg class="contact-icon" viewBox="0 0 40 40" fill="none" stroke="currentColor" stroke-width="3"><rect x="5" y="8" width="30" height="20"/><path d="M14 33h12M20 28v5"/></svg>krcoatfoamsealers.com</li>
    </ul>
  </section>

</main>
</body>
</html>
```